professional business card

Professional business card with logo on one side, and underneath logo list:
- power
-data
-fibre optic
-isolar

On other side:
Marcus Trent
Owner
MOB 0492 738 204
marcus@vorpa.com.au
www.vorpaelectrical.com.au

Please edit logo to just leave VORPA

```html
<!DOCTYPE html>
<html lang="en">
<head>
<meta charset="utf-8">
<title>Vorpa Electrical – Business Card</title>
<link href="https://fonts.googleapis.com/css2?family=Roboto:wght@300;400;500&display=swap" rel="stylesheet">
<style>
  :root {
    --backdrop: #3a3a3c;
    --card: #232325;
    --teal: #12959b;
    --white: #e9e9ea;
    --muted: #8d8e91;
    --strip: #77787b;
  }
  * { margin: 0; padding: 0; box-sizing: border-box; }
  html, body {
    width: 799px; height: 1200px; overflow: hidden;
    background: var(--backdrop);
    font-family: "Roboto", sans-serif;
  }
  .card {
    position: absolute; left: 80px;
    width: 640px; height: 366px;
    background: var(--card);
    border-radius: 3px;
    box-shadow: 0 14px 30px rgba(0,0,0,.45);
    overflow: hidden;
  }
  .card--front { top: 150px; }
  .card--back { top: 690px; }

  .brand-name {
    color: var(--teal);
    font-weight: 500;
    letter-spacing: 2px;
    line-height: 1;
  }
  .card--front .brand-name {
    position: absolute; left: 150px; top: 92px; font-size: 84px;
  }
  .services {
    position: absolute; left: 152px; top: 200px;
    color: var(--muted); font-size: 15px; font-weight: 300;
    letter-spacing: 1.5px; text-transform: uppercase;
  }
  .services .sep { color: var(--teal); margin: 0 8px; }
  .website {
    position: absolute; left: 152px; top: 272px;
    color: var(--muted); font-size: 15px; font-weight: 300;
  }

  .card--back .brand-name {
    position: absolute; left: 60px; top: 92px; font-size: 66px;
  }
  .contact {
    position: absolute; left: 380px; top: 118px;
  }
  .contact__name { color: var(--teal); font-size: 24px; font-weight: 400; }
  .contact__role { color: var(--white); font-size: 13px; margin-top: 2px; }
  .contact__list { list-style: none; margin-top: 22px; }
  .contact__list li {
    display: flex; align-items: center; gap: 10px;
    color: var(--white); font-size: 16px; margin-bottom: 6px;
  }
  .contact__list svg { width: 13px; height: 13px; fill: var(--teal); flex: none; }

  .strip {
    position: absolute; left: 0; bottom: 0; width: 100%; height: 90px;
  }
  .licence {
    position: absolute; right: 52px; bottom: 34px;
    color: var(--white); font-size: 17px; letter-spacing: 9px;
  }
</style>
</head>
<body>

<section class="card card--front">
  <div class="brand-name">VORPA</div>
  <div class="services">Power<span class="sep">|</span>Data<span class="sep">|</span>Fibre Optic<span class="sep">|</span>iSolar</div>
  <div class="website">www.vorpaelectrical.com.au</div>
</section>

<section class="card card--back">
  <div class="brand-name">VORPA</div>

  <div class="contact">
    <div class="contact__name">Marcus Trent</div>
    <div class="contact__role">Owner</div>
    <ul class="contact__list">
      <li>
        <svg viewBox="0 0 16 16"><path d="M3 1h3l1.5 4-2 1.3a9 9 0 0 0 4.2 4.2L11 8.5l4 1.5v3a2 2 0 0 1-2 2A12 12 0 0 1 1 3a2 2 0 0 1 2-2z"/></svg>
        0492 738 204
      </li>
      <li>
        <svg viewBox="0 0 16 16"><path d="M1 3h14v10H1z M2 4l6 5 6-5" stroke="#232325" stroke-width="1.2"/></svg>
        marcus@vorpa.com.au
      </li>
      <li>
        <svg viewBox="0 0 16 16"><circle cx="8" cy="8" r="7"/><path d="M1 8h14M8 1c-3 3-3 11 0 14M8 1c3 3 3 11 0 14" stroke="#232325" stroke-width="1" fill="none"/></svg>
        vorpaelectrical.com.au
      </li>
    </ul>
  </div>

  <svg class="strip" viewBox="0 0 640 90" preserveAspectRatio="none">
    <rect x="0" y="14" width="320" height="8" fill="var(--strip)"/>
    <path d="M300 90 L300 34 Q300 14 320 14 L640 14 L640 90 Z" fill="var(--teal)"/>
  </svg>
  <div class="licence">EC20583</div>
</section>

</body>
</html>
```